TRV Consulting Website Design
New Website for Consulting company
Project: TRV Consulting Website Design
TRV Consulting Website Design - Consulting
Creative Brief
Consulting
www.trvconsulting-example.com
Logistics consulting focused in Bulk Logistics, Freight Rail, Energy and Chemical sectors with Investment Advisory expertise in the respective sectors. An expert team of industry veterans who partner with clients to design custom logistics solutions with extensive experience in logistics infrastructure design, supply chain assessments, strategic planning, and due diligence projects.
Likes: Clean, crisp, professional imagery Dislikes: Too much text, cluttered, busy sights
Modern
You choose
top
http://www.morwayfreight-example.com/
We have a newly designed logo which we want to use. We are open to changing the colors in the logo as well. Also, the design must be mobile friendly and will be implemented in Bootstrap 3.
torvell torvell
Don't focus on tanker trains and cars Don't focus on human hands

```html
<!DOCTYPE html>
<html lang="en">
<head>
<meta charset="utf-8">
<title>TRV Consulting</title>
<link rel="stylesheet" href="https://fonts.googleapis.com/css2?family=Exo+2:ital,wght@0,500;0,600;0,700;1,600&family=Open+Sans:wght@400;600&display=swap">
<style>
  :root {
    --navy: #0f3f63;
    --orange: #f39a14;
    --ink: #333;
    --muted: #4a4a4a;
    --card-top: #f7f7f7;
    --card-bottom: #e4e4e4;
    --footer: #4a4a4a;
    --social: #d9d9d9;
    --white: #fff;
  }
  * { box-sizing: border-box; margin: 0; padding: 0; }
  html, body { width: 1200px; height: 998px; overflow: hidden; background: var(--white); }
  body { position: relative; font-family: "Open Sans", Arial, sans-serif; color: var(--ink); }

  .site-header { position: absolute; left: 0; top: 0; width: 1200px; height: 143px; background: var(--white); }
  .brand { position: absolute; left: 132px; top: 32px; display: flex; align-items: center; gap: 12px; }
  .brand-mark { width: 52px; height: 52px; background: var(--orange); }
  .brand-name { font-family: "Exo 2", sans-serif; font-weight: 700; font-size: 28px; color: var(--navy); letter-spacing: 1px; }

  .phone { position: absolute; left: 836px; top: 16px; width: 230px; height: 44px; }
  .phone-bg { position: absolute; inset: 0; background: var(--navy); clip-path: polygon(6% 0, 100% 0, 94% 100%, 0 100%); }
  .phone-icon { position: absolute; left: 14px; top: 6px; width: 40px; height: 32px; background: var(--orange); clip-path: polygon(20% 0, 100% 0, 80% 100%, 0 100%); display: flex; align-items: center; justify-content: center; }
  .phone-number { position: absolute; left: 66px; top: 0; line-height: 44px; font-family: "Exo 2", sans-serif; font-weight: 600; font-size: 19px; color: var(--white); }

  .main-nav { position: absolute; left: 434px; top: 88px; width: 640px; height: 26px; }
  .main-nav a { position: absolute; top: 0; font-family: "Exo 2", sans-serif; font-weight: 600; font-size: 20px; line-height: 26px; color: var(--navy); text-decoration: none; white-space: nowrap; }
  .main-nav a.active { color: var(--orange); }

  .hero { position: absolute; left: 0; top: 143px; width: 1200px; height: 415px;
    background:
      radial-gradient(ellipse 230px 260px at 230px 300px, rgba(226,234,244,.95), rgba(226,234,244,0) 100%),
      radial-gradient(ellipse 150px 240px at 830px 270px, rgba(170,190,215,.8), rgba(170,190,215,0) 100%),
      radial-gradient(ellipse 260px 120px at 950px 90px, rgba(200,80,50,.45), rgba(200,80,50,0) 100%),
      radial-gradient(ellipse 220px 160px at 560px 150px, rgba(230,170,110,.55), rgba(230,170,110,0) 100%),
      linear-gradient(180deg, #8a6a4e 0%, #a57f5a 45%, #6b5446 100%); }
  .hero-arrow { position: absolute; top: 183px; width: 54px; height: 42px; background: rgba(60,60,60,.75); display: flex; align-items: center; justify-content: center; }
  .hero-arrow.prev { left: 0; }
  .hero-arrow.next { right: 0; }
  .hero-caption { position: absolute; left: 135px; top: 340px; width: 572px; height: 54px; background: rgba(30,30,30,.72); clip-path: polygon(4% 0, 100% 0, 96% 100%, 0 100%); }
  .hero-caption span { position: absolute; left: 26px; top: 0; line-height: 54px; font-family: "Exo 2", sans-serif; font-style: italic; font-weight: 600; font-size: 26px; color: var(--white); letter-spacing: .5px; }

  .card { position: absolute; top: 604px; width: 283px; height: 313px; background: linear-gradient(var(--card-top), var(--card-bottom)); box-shadow: 0 6px 10px rgba(0,0,0,.18); border-radius: 4px; }
  .card-title { height: 46px; background: var(--navy); border-radius: 4px 4px 0 0; text-align: center; line-height: 46px; font-family: "Exo 2", sans-serif; font-weight: 600; font-size: 22px; color: var(--white); }
  .card-image { position: absolute; left: 14px; top: 62px; width: 255px; height: 149px; border: 3px solid var(--white); }
  .card-text { position: absolute; left: 18px; top: 222px; width: 250px; font-size: 12px; line-height: 19px; color: var(--muted); white-space: nowrap; }
  .card-more { position: absolute; left: 128px; top: 280px; width: 28px; height: 26px; background: var(--orange); color: var(--white); font-weight: 700; font-size: 24px; line-height: 24px; text-align: center; }

  .site-footer { position: absolute; left: 0; top: 950px; width: 1200px; height: 48px; background: var(--footer); }
  .copyright { position: absolute; left: 135px; top: 0; line-height: 48px; font-size: 12px; color: #ddd; }
  .social { position: absolute; left: 893px; top: 14px; display: flex; gap: 18px; }
  .social span { width: 20px; height: 20px; border-radius: 50%; background: var(--social); }
</style>
</head>
<body>
  <header class="site-header">
    <div class="brand"><div class="brand-mark"></div><div class="brand-name">TRV CONSULTING</div></div>
    <div class="phone">
      <div class="phone-bg"></div>
      <div class="phone-icon">
        <svg width="18" height="18" viewBox="0 0 24 24"><path fill="#fff" d="M6.6 10.8a15 15 0 0 0 6.6 6.6l2.2-2.2c.3-.3.7-.4 1-.2 1.1.4 2.3.6 3.6.6.6 0 1 .4 1 1V20c0 .6-.4 1-1 1A17 17 0 0 1 3 4c0-.6.4-1 1-1h3.5c.6 0 1 .4 1 1 0 1.3.2 2.5.6 3.6.1.3 0 .7-.2 1z"/></svg>
      </div>
      <div class="phone-number">+1-555-014-2290</div>
    </div>
    <nav class="main-nav">
      <a class="active" style="left:0">HOME</a>
      <a style="left:89px">ABOUT US</a>
      <a style="left:215px">OUR SERVICES</a>
      <a style="left:383px">INSIGHTS</a>
      <a style="left:505px">CONTACT US</a>
    </nav>
  </header>

  <section class="hero" role="img" aria-label="Consultant with tablet in a warehouse, staff checking shelves behind him">
    <div class="hero-arrow prev"><svg width="14" height="18" viewBox="0 0 14 18"><path d="M10 2 3 9l7 7" stroke="#fff" stroke-width="3" fill="none"/></svg></div>
    <div class="hero-arrow next"><svg width="14" height="18" viewBox="0 0 14 18"><path d="m4 2 7 7-7 7" stroke="#fff" stroke-width="3" fill="none"/></svg></div>
    <div class="hero-caption"><span>WE ARE LOGISTICS CONSULTING COMPANY</span></div>
  </section>

  <article class="card" style="left:130px">
    <div class="card-title">ABOUT TRV</div>
    <div class="card-image" role="img" aria-label="Business team reviewing documents together" style="background:radial-gradient(ellipse 80px 90px at 70px 90px,#2e333b,rgba(46,51,59,0)),radial-gradient(ellipse 70px 80px at 170px 70px,#c9a58c,rgba(201,165,140,0)),linear-gradient(90deg,#f1f1f1,#d8d4d0 55%,#6c6f76)"></div>
    <p class="card-text">Lorem ipsum dolor sit amet, consectetuero<br>adipiscing elit, sed diam nonummy.</p>
    <div class="card-more">+</div>
  </article>

  <article class="card" style="left:458px">
    <div class="card-title">OUR SERVICES</div>
    <div class="card-image" role="img" aria-label="Rail yard workers in hard hats beside a locomotive" style="background:radial-gradient(ellipse 80px 70px at 60px 70px,#a3261e,rgba(163,38,30,0)),radial-gradient(ellipse 60px 80px at 180px 100px,#4c4f55,rgba(76,79,85,0)),linear-gradient(180deg,#c6d3e0,#8c8f92 60%,#6e6a64)"></div>
    <p class="card-text">Lorem ipsum dolor sit amet, consectetuero<br>adipiscing elit, sed diam nonummy.</p>
    <div class="card-more">+</div>
  </article>

  <article class="card" style="left:785px">
    <div class="card-title">INSIGHTS</div>
    <div class="card-image" role="img" aria-label="Industrial plant and rail tank cars at dusk" style="background:radial-gradient(ellipse 90px 50px at 180px 95px,#2d3a4a,rgba(45,58,74,0)),radial-gradient(ellipse 90px 40px at 70px 100px,#6f9a4a,rgba(111,154,74,0)),linear-gradient(180deg,#7f86c4,#c08aa2 40%,#5f6a58 75%,#3a3f34)"></div>
    <p class="card-text">Lorem ipsum dolor sit amet, consectetuero<br>adipiscing elit, sed diam nonummy.</p>
    <div class="card-more">+</div>
  </article>

  <footer class="site-footer">
    <p class="copyright">Copyright © 2015 TRV Consulting. All right reserved.</p>
    <div class="social"><span></span><span></span><span></span><span></span><span></span><span></span></div>
  </footer>
</body>
</html>
```